Commercial Flooring Contractor Website ($100 Bonus)

We are working with a new commercial flooring contractor in California. They work on schools, hospitals, and government projects.
A few websites for inspiration:
https://trimcoverwork.example (These guys are competitors and provide the same work our client does).
https://zqpavingsco.example (Although NOT a contractor, the simplicity of this site is stunning).
https://www.quietrapid.example (NOT a flooring contractor, but this site is modern, and has a boldness to it).
https://www.dawnfoldatelier.example/en-us (website for an Architectural office that is clean and showcases their work. I can see this working for a flooring contractor).
Thank you for taking the time to consider designing a website for us. We are web developers based in Stockton, CA, USA. Most of our projects go through the same process. Understanding this process may help you win a project with us. We custom-code all of our websites in-house. We don’t have any requirements as to what tools you use for your design, but we ask that you follow these guidelines.
IMAGES:
If you use any images or icons in the design, we ask that you have a link to the asset so we can purchase the image/icon. Most of the designs we submit do not have the customer’s images on them unless they have some great images. Be creative; show us the feeling you are trying to portray with your image choices. Use any royalty-free site you choose. We subscribe to Velto and mainly use their images, but we can purchase images outside of Velto.
FONTS:
We ask that you identify the fonts you’re using in the design. This can be done in a message if you want. We typically use Google Fonts and Velto Fonts.
CONTENT:
We're always open to different content and ideas. We often submit designs with stock images so the client can see our vision. We typically take pictures after the website launch to use their images with our vision. Lorem Ipsum is fine for paragraphs, but we ask that you make the Headers with correct English. We want to be able to show the vision and identify the sections of the website.
INSPIRATION:
We typically add a couple of links in the brief of websites we like to help you get started in your design.
REVISIONS:
We do not often ask for revisions of the designs unless we see something in the design that may not appeal to the client. If there are slight changes that we want to make, we do that in the development process.
FEEDBACK:
We rarely give feedback on designs during the design process. We are working on many website projects and do not have the time to provide feedback. We usually respond if your request is well thought out and asks specific questions, but a note asking “feedback, please” usually goes unanswered.
1 page

```html
<!DOCTYPE html>
<html lang="en">
<head>
<meta charset="utf-8">
<title>True Grain – Commercial Flooring Contractor</title>
<link href="https://fonts.googleapis.com/css2?family=Oswald:wght@500;600;700&family=Mulish:wght@400;600;700;800&display=swap" rel="stylesheet">
<style>
:root{
  --red:#f0574f;
  --dark:#222222;
  --ink:#2b2b2b;
  --text:#555555;
  --muted:#777777;
  --paper:#f1f1f1;
  --slate:#5c6462;
  --footer:#2a2a2a;
  --white:#ffffff;
}
*{margin:0;padding:0;box-sizing:border-box}
html,body{width:1200px;height:3893px;overflow:hidden;background:var(--white)}
body{position:relative;font-family:'Mulish',sans-serif;color:var(--text)}
.abs{position:absolute}
.head{font-family:'Oswald',sans-serif;font-weight:600;text-transform:uppercase;color:var(--dark)}
.red{color:var(--red)}

/* header */
.topbar{left:0;top:0;width:1200px;height:73px;background:var(--white);z-index:3}
.brand{left:126px;top:10px;width:134px;height:134px;border-radius:50%;background:var(--white);z-index:4;display:flex;align-items:center;justify-content:center;box-shadow:0 2px 6px rgba(0,0,0,.15)}
.brand-ring{width:112px;height:112px;border-radius:50%;border:3px solid var(--red);display:flex;align-items:center;justify-content:center;font-family:'Oswald',sans-serif;font-weight:600;font-size:20px;color:var(--dark);text-transform:uppercase;text-align:center;line-height:1.05}
.nav{left:399px;top:28px;display:flex;gap:38px;font-size:12.5px;letter-spacing:1.6px;font-weight:600;color:var(--dark);z-index:5;white-space:nowrap}
.nav .on{color:var(--red);position:relative}
.nav .on::after{content:"";position:absolute;left:0;right:0;bottom:-9px;height:2px;background:var(--red)}
.btn{background:var(--red);color:var(--white);font-weight:700;letter-spacing:1.6px;text-transform:uppercase;display:flex;align-items:center;justify-content:center;white-space:nowrap}
.nav-btn{left:895px;top:19px;width:173px;height:34px;font-size:12px;z-index:5}

/* hero */
.hero{left:0;top:73px;width:1200px;height:634px;background:linear-gradient(180deg,#3a3d40 0%,#5b5f63 45%,#6e5d4e 70%,#4a3d33 100%)}
.hero-title{left:0;top:385px;width:1200px;text-align:center;font-size:44px;color:var(--white);letter-spacing:.5px}
.hero-btn{left:487px;top:465px;width:226px;height:45px;font-size:15px}
.dots{left:563px;top:653px;display:flex;gap:8px}
.dots i{width:8px;height:8px;border-radius:50%;background:var(--white);display:block}
.dots i.on{background:var(--red)}

/* services grid */
.tile{overflow:hidden}
.tile-label{position:absolute;left:20px;bottom:26px;font-family:'Oswald',sans-serif;font-weight:600;font-size:19px;color:var(--white);text-transform:uppercase}
.tile-shade{position:absolute;inset:0;background:linear-gradient(180deg,rgba(0,0,0,0) 55%,rgba(0,0,0,.55) 100%)}
.tile-note{position:absolute;left:19px;bottom:22px;width:260px;font-size:12px;line-height:1.4;color:var(--white)}
.tile-btn{position:absolute;right:21px;bottom:26px;width:80px;height:26px;font-size:10px;letter-spacing:.5px}

/* welcome */
.welcome{left:8px;top:1327px;width:1181px;height:535px;background:var(--paper)}
.welcome-side{left:1118px;top:1327px;width:71px;height:535px;overflow:hidden}
.welcome-side span{position:absolute;left:-232px;top:232px;width:535px;transform:rotate(-90deg);font-family:'Oswald',sans-serif;font-weight:700;font-size:76px;line-height:71px;color:var(--white);text-transform:uppercase;text-align:center;white-space:nowrap}
.welcome-title{left:651px;top:1385px;font-size:27px}
.welcome-copy{left:651px;top:1467px;width:416px;font-size:13.5px;line-height:1.43;color:#555}
.welcome-copy p+p{margin-top:22px}
.welcome-btn{left:655px;top:1746px;width:102px;height:34px;font-size:12px;letter-spacing:.3px}

/* works */
.section-title{left:0;width:1200px;text-align:center;font-size:27px}
.title-rule{height:3px;background:var(--dark)}
.work-name{font-size:19px;text-align:center}
.work-text{font-size:12.5px;line-height:1.5;text-align:center;color:var(--muted)}

/* why choose */
.why{left:0;top:2637px;width:1200px;height:609px;background:var(--slate)}
.why-ring{left:133px;top:2688px;width:518px;height:518px;border-radius:50%;background:#6c7371}
.why-photo{left:149px;top:2704px;width:486px;height:486px;border-radius:50%;background:linear-gradient(135deg,#d7a879 0%,#c89162 40%,#e9e9ea 65%,#f4f4f4 100%)}
.why-title{left:692px;top:2708px;font-size:27px;color:var(--white)}
.why-copy{left:694px;top:2800px;width:372px;font-size:13.5px;line-height:1.42;color:var(--white)}
.perks{left:705px;top:2952px;width:316px}
.perk{display:flex;align-items:center;gap:16px;height:52px;border-bottom:1px solid rgba(255,255,255,.35);padding-left:20px;font-size:13.5px;font-weight:800;color:var(--white);text-transform:uppercase}
.perk:last-child{border-bottom:none}
.perk svg{width:22px;height:22px;flex:none}

/* cta */
.cta{left:0;top:3246px;width:1200px;height:284px;background:var(--red)}
.cta-title{left:0;top:3306px;width:1200px;text-align:center;font-size:26px;color:var(--white)}
.cta-copy{left:0;top:3368px;width:1200px;text-align:center;font-size:13.5px;line-height:1.45;color:var(--white)}
.cta-btn{left:524px;top:3423px;width:153px;height:47px;border:2px solid var(--white);color:var(--white);font-size:14px;font-weight:800;letter-spacing:.5px;display:flex;align-items:center;justify-content:center}

/* footer */
.footer{left:0;top:3530px;width:1200px;height:363px;background:var(--footer)}
.foot-brand{left:135px;top:3575px;width:210px;height:210px;border-radius:50%;border:3px solid var(--white);display:flex;align-items:center;justify-content:center;font-family:'Oswald',sans-serif;font-weight:600;font-size:40px;color:var(--white);text-transform:uppercase;text-align:center;line-height:1.05}
.foot-head{font-size:13.5px;font-weight:800;color:var(--white);text-transform:uppercase;padding-bottom:10px;border-bottom:2px solid var(--white)}
.foot-item{display:flex;align-items:center;gap:11px;font-size:11.5px;line-height:1.4;color:var(--white);white-space:nowrap}
.foot-ico{width:23px;height:23px;border-radius:50%;background:var(--white);flex:none;display:flex;align-items:center;justify-content:center}
.foot-ico svg{width:13px;height:13px}
.foot-menu{font-size:11.5px;line-height:23px;color:var(--white);text-transform:uppercase}
.foot-rule{left:134px;top:3808px;width:934px;height:1px;background:rgba(255,255,255,.6)}
.copyright{left:0;top:3845px;width:1200px;text-align:center;font-size:11px;color:var(--white)}
</style>
</head>
<body>

<!-- header -->
<div class="abs topbar"></div>
<div class="abs brand"><div class="brand-ring">True<br>Grain</div></div>
<nav class="abs nav">
  <span class="on">HOME</span><span>ABOUT US</span><span>SERVICES</span><span>BLOG</span><span>CONTACT US</span>
</nav>
<div class="abs btn nav-btn">Free Consultation</div>

<!-- hero -->
<div class="abs hero" role="img" aria-label="Empty modern office corridor with glass walls and polished wood floor"></div>
<h1 class="abs head hero-title">Commercial Flooring Contractor</h1>
<div class="abs btn hero-btn">Free Consultation</div>
<div class="abs dots"><i></i><i></i><i class="on"></i><i></i><i></i></div>

<!-- services grid -->
<div class="abs tile" style="left:8px;top:718px;width:388px;height:292px;background:linear-gradient(160deg,#c9cdd0,#8e9397 60%,#5c4d44)" role="img" aria-label="Worker polishing a concrete floor with a floor machine">
  <div class="tile-shade"></div>
  <div class="tile-label" style="bottom:68px">Concrete</div>
  <div class="tile-note">Lorem Ipsum is simply dummy text of the printing and typesetting industry</div>
  <div class="btn tile-btn">Read More</div>
</div>
<div class="abs tile" style="left:405px;top:718px;width:387px;height:292px;background:linear-gradient(160deg,#3f8fd0,#b9a595 45%,#a89484)" role="img" aria-label="Hands in gloves spreading a textured floor coating">
  <div class="tile-shade"></div><div class="tile-label">Coatings</div>
</div>
<div class="abs tile" style="left:802px;top:718px;width:388px;height:292px;background:linear-gradient(160deg,#c7c9cb,#a9acae 55%,#8a7b6c)" role="img" aria-label="Installer laying a large grey floor tile">
  <div class="tile-shade"></div><div class="tile-label">Tile</div>
</div>
<div class="abs tile" style="left:8px;top:1020px;width:388px;height:293px;background:linear-gradient(150deg,#b07b4f,#8a5a36 50%,#c7b9a8)" role="img" aria-label="Hand fitting a wooden floor plank">
  <div class="tile-shade"></div><div class="tile-label">Wood</div>
</div>
<div class="abs tile" style="left:405px;top:1020px;width:387px;height:293px;background:linear-gradient(180deg,#dfe0e1,#b4b6b8 60%,#8e9092)" role="img" aria-label="Worker rolling an overlay onto a glossy floor">
  <div class="tile-shade"></div><div class="tile-label">Overlays</div>
</div>
<div class="abs tile" style="left:802px;top:1020px;width:388px;height:293px;background:linear-gradient(180deg,#d9dadb,#9fa2a4 60%,#707375)" role="img" aria-label="Hand spreading self-leveling compound with a trowel">
  <div class="tile-shade"></div><div class="tile-label">Vapor Control &amp; Self-Leveling</div>
</div>

<!-- welcome -->
<div class="abs welcome"></div>
<div class="abs welcome-side"><span>True Grain</span></div>
<div class="abs" style="left:134px;top:1389px;width:476px;height:396px;background:linear-gradient(180deg,#5b5f78 0%,#9a8d7a 30%,#c79a62 60%,#b5844f 100%)" role="img" aria-label="School gymnasium with a polished hardwood floor"></div>
<h2 class="abs head welcome-title">Welcome to <span class="red">True Grain</span></h2>
<div class="abs welcome-copy">
  <p>It is a long established fact that a reader will be distracted by the readable content of a page when looking at its layout. The point of using Lorem Ipsum is that it has a more-or-less normal distribution of letters, as opposed to using 'Content here, content here', making it look like readable English. Many desktop publishing packages and web page editors now use Lorem Ipsum as their default model text</p>
  <p>If you are going to use a passage of Lorem Ipsum, you need to be sure there isn't anything embarrassing hidden in the middle of text. All the Lorem Ipsum generators on the Internet tend to repeat predefined chunks as necessary</p>
</div>
<div class="abs btn welcome-btn">Read More</div>

<!-- our works -->
<h2 class="abs head section-title" style="top:1915px">Our <span class="red">Works</span></h2>
<div class="abs title-rule" style="left:538px;top:1964px;width:124px"></div>

<div class="abs" style="left:32px;top:2053px;width:365px;height:375px;background:linear-gradient(180deg,#e9f0f4,#c9d6de 55%,#e3e8ea)" role="img" aria-label="Bright hospital corridor with light tiled floor"></div>
<div class="abs" style="left:416px;top:2016px;width:365px;height:450px;background:linear-gradient(180deg,#eceded,#c9c7c1 40%,#5868a8 55%,#dadbe0)" role="img" aria-label="School hallway with lockers and checkered floor"></div>
<div class="abs" style="left:801px;top:2053px;width:366px;height:375px;background:linear-gradient(120deg,#9c9c9c,#dcdcdc 45%,#f6f6f6 70%,#5b5b5b)" role="img" aria-label="Government building corridor with white glossy floor"></div>

<h3 class="abs head work-name" style="left:32px;top:2460px;width:365px">Hospitals</h3>
<p class="abs work-text" style="left:62px;top:2500px;width:305px">t is a long established fact that a reader will be distracted by the readable content</p>
<h3 class="abs head work-name" style="left:416px;top:2497px;width:365px">School</h3>
<p class="abs work-text" style="left:446px;top:2537px;width:305px">t is a long established fact that a reader will be distracted by the readable content</p>
<h3 class="abs head work-name" style="left:801px;top:2460px;width:366px">Government</h3>
<p class="abs work-text" style="left:831px;top:2500px;width:305px">t is a long established fact that a reader will be distracted by the readable content</p>

<!-- why choose us -->
<div class="abs why"></div>
<div class="abs why-ring"></div>
<div class="abs why-photo" role="img" aria-label="Gloved hand tapping a wooden floor plank into place with a hammer"></div>
<h2 class="abs head why-title">Why Choose Us</h2>
<div class="abs title-rule" style="left:692px;top:2762px;width:52px;background:var(--white)"></div>
<p class="abs why-copy">It is a long established fact that a reader will be distracted by the readable content of a page when looking at its layout. The point of using Lorem Ipsum is that it has a more-or-less normal distribution aking this the first true generator on the Internet. It uses a dictionary of over 200 Latin words.</p>
<div class="abs perks">
  <div class="perk"><svg viewBox="0 0 24 24" fill="none" stroke="#fff" stroke-width="2"><path d="M12 2l8 3v6c0 5-3.5 9-8 11-4.5-2-8-6-8-11V5z"/><path d="M8.5 12l2.5 2.5 4.5-5"/></svg>All Work Guaranteed</div>
  <div class="perk"><svg viewBox="0 0 24 24" fill="none" stroke="#fff" stroke-width="2"><circle cx="12" cy="12" r="7"/><path d="M12 8v8M9.5 10h4a1.5 1.5 0 010 3h-3a1.5 1.5 0 000 3h4"/></svg>Flexible Payment Options</div>
  <div class="perk"><svg viewBox="0 0 24 24" fill="#fff"><path d="M5 2h10l4 4v16H5z"/><path d="M8 11h8M8 14h8M8 17h6" stroke="#5c6462" stroke-width="1.6"/></svg>Free Service Estimates</div>
  <div class="perk"><svg viewBox="0 0 24 24" fill="none" stroke="#fff" stroke-width="2"><path d="M12 3l10 6-10 6L2 9z"/><path d="M2 14l10 6 10-6"/></svg>Locally Owned</div>
</div>

<!-- call to action -->
<div class="abs cta"></div>
<h2 class="abs head cta-title">Let's Get Started With Your Flooring Project!</h2>
<p class="abs cta-copy">It is a long established fact that a reader will be distracted by the readable content of a page when<br>looking at its layout. The point of using Lorem Ipsum is that it has a more-or-less normal distribution</p>
<div class="abs cta-btn">CONTACT US</div>

<!-- footer -->
<div class="abs footer"></div>
<div class="abs foot-brand">True<br>Grain</div>

<div class="abs foot-head" style="left:424px;top:3580px;width:192px">Contact Us</div>
<div class="abs foot-item" style="left:424px;top:3632px"><span class="foot-ico"><svg viewBox="0 0 24 24" fill="#2a2a2a"><path d="M12 2a7 7 0 00-7 7c0 5 7 13 7 13s7-8 7-13a7 7 0 00-7-7zm0 9.5A2.5 2.5 0 1112 6.5a2.5 2.5 0 010 5z"/></svg></span>Marlow Bay, CA</div>
<div class="abs foot-item" style="left:424px;top:3681px"><span class="foot-ico"><svg viewBox="0 0 24 24" fill="#2a2a2a"><path d="M6.6 10.8a15 15 0 006.6 6.6l2.2-2.2a1 1 0 011-.25 11.4 11.4 0 003.6.57 1 1 0 011 1V20a1 1 0 01-1 1A17 17 0 013 4a1 1 0 011-1h3.5a1 1 0 011 1c0 1.25.2 2.45.57 3.6a1 1 0 01-.25 1z"/></svg></span><span>Call Us<br>+1 555 010 0199</span></div>
<div class="abs foot-item" style="left:424px;top:3733px"><span class="foot-ico"><svg viewBox="0 0 24 24" fill="#2a2a2a"><path d="M3 5h18v14H3z"/><path d="M3 6l9 7 9-7" stroke="#fff" stroke-width="1.8" fill="none"/></svg></span><span>E mail Us<br>info@truegrain.example</span></div>

<div class="abs foot-head" style="left:735px;top:3580px;width:107px">Menu</div>
<div class="abs foot-menu" style="left:737px;top:3620px">Home<br>About Us<br>Services<br>Blog<br>Contact Us</div>

<div class="abs foot-head" style="left:965px;top:3580px;width:107px">Follow Us</div>
<div class="abs foot-item" style="left:964px;top:3640px"><span class="foot-ico"></span><span>Like us on<br>PAGEBOARD</span></div>
<div class="abs foot-item" style="left:964px;top:3690px"><span class="foot-ico"></span><span>Follow us on<br>CHIRPLINE</span></div>
<div class="abs foot-item" style="left:964px;top:3741px"><span class="foot-ico"></span><span>Follow us on<br>WORKLINK</span></div>

<div class="abs foot-rule"></div>
<p class="abs copyright">Copyright © 2023 All Rights Reserved</p>

</body>
</html>
```